Zielgruppe
Beratung und Live-Kommunikation
Aufgabenstellung
- Re-Design vom Firmenlogo und Briefpapier
- Anpassung/ Abwandlung der vorhandenen Elemente (Briefkopf). Anordnung, Schrift, etc.
- Ideen, wie man den Inhalt (den Tätigkeitsbereich) ggfs. grafisch ansprechend als Logo darstellen kann.
- Klare Linien, symmetrisch. Schwarz-weiß/keine Farbe
- Briefpapier auf *.doc Basis, kein randloser Druck
- derzeitiger Stil siehe www.buehnenwerkraum.de

```html
<!DOCTYPE html>
<html lang="de">
<head>
<meta charset="utf-8">
<title>Briefpapier – Wellbrock Produktionsbüro</title>
<link href="https://fonts.googleapis.com/css2?family=Questrial&family=Montserrat:wght@700&display=swap" rel="stylesheet">
<style>
  :root {
    --ink: #111111;
    --text: #333333;
    --mark: #9a9a9a;
    --paper: #ffffff;
  }
  html, body { margin: 0; padding: 0; overflow: hidden; background: var(--paper); }
  .letterhead {
    position: relative; width: 858px; height: 1200px; overflow: hidden;
    background: var(--paper); color: var(--ink);
    font-family: "Questrial", "Century Gothic", sans-serif;
  }
  .abs { position: absolute; margin: 0; }

  .brand { right: 38px; top: 100px; font-size: 24px; line-height: 28px; font-weight: 400; color: var(--ink); }

  .services { right: 38px; top: 164px; list-style: none; padding: 0; }
  .services li { display: flex; align-items: center; justify-content: flex-end; height: 24px; font-size: 20px; }
  .services svg { width: 20px; height: 20px; margin-right: 7px; }

  .window-mark { width: 10px; height: 10px; border-color: var(--mark); border-style: solid; border-width: 0; }
  .wm-tl { left: 97px; top: 183px; border-top-width: 1px; border-left-width: 1px; }
  .wm-tr { left: 436px; top: 183px; border-top-width: 1px; border-right-width: 1px; }
  .wm-bl { left: 97px; top: 353px; border-bottom-width: 1px; border-left-width: 1px; }
  .wm-br { left: 436px; top: 353px; border-bottom-width: 1px; border-right-width: 1px; }
  .sender { left: 117px; top: 192px; font-size: 11.5px; color: var(--ink); }

  .fold-mark { width: 11px; height: 0; border-top: 1px solid var(--mark); }
  .fold-1 { left: 13px; top: 428px; }
  .fold-1r { left: 834px; top: 428px; }
  .punch-mark { left: 13px; top: 855px; }

  .contact { left: 594px; width: 250px; font-size: 11.5px; line-height: 14px; color: var(--text); }
  .contact-row { display: flex; align-items: flex-start; }
  .contact-row svg { width: 18px; height: 18px; flex: none; margin-right: 10px; margin-top: -2px; }
  .company { font-family: "Montserrat", sans-serif; font-weight: 700; font-size: 10.6px; color: var(--ink); }

  .payment-note { left: 97px; top: 1088px; width: 463px; font-size: 12px; line-height: 14px; color: var(--text); }
</style>
</head>
<body>
<main class="letterhead">

  <header class="brand abs">Wellbrock Produktionsbüro</header>

  <ul class="services abs">
    <li><svg viewBox="0 0 20 20"><rect width="20" height="20" rx="3" fill="#111"/><rect x="4" y="5" width="12" height="8" rx="1" fill="none" stroke="#fff" stroke-width="1.5"/><path d="M7 13 L7 16 L10 13" fill="#fff"/></svg>beratung</li>
    <li><svg viewBox="0 0 20 20"><rect width="20" height="20" rx="3" fill="#111"/><circle cx="10" cy="8" r="4.5" fill="#fff"/><rect x="8" y="12" width="4" height="4" fill="#fff"/></svg>planung</li>
    <li><svg viewBox="0 0 20 20"><rect width="20" height="20" rx="3" fill="#111"/><circle cx="10" cy="10" r="6" fill="none" stroke="#fff" stroke-width="2" stroke-dasharray="2 1.5"/><circle cx="10" cy="10" r="2.5" fill="#fff"/></svg>umsetzung</li>
  </ul>

  <span class="window-mark wm-tl abs"></span>
  <span class="window-mark wm-tr abs"></span>
  <span class="window-mark wm-bl abs"></span>
  <span class="window-mark wm-br abs"></span>
  <p class="sender abs">Wellbrock &nbsp;|&nbsp; Lindenweg 7 &nbsp;|&nbsp; D-51789 Musterstadt</p>

  <span class="fold-mark fold-1 abs"></span>
  <span class="fold-mark fold-1r abs"></span>
  <span class="fold-mark punch-mark abs"></span>

  <div class="contact abs" style="top:845px">
    <div class="contact-row">
      <svg viewBox="0 0 18 18"><rect width="18" height="18" rx="3" fill="#111"/><path d="M9 3.5a4 4 0 0 1 4 4c0 3-4 7-4 7s-4-4-4-7a4 4 0 0 1 4-4z" fill="none" stroke="#fff" stroke-width="1.4"/></svg>
      <div><span class="company">wellbrock production office GmbH</span><br>Lindenweg 7<br>D-51789 Musterstadt</div>
    </div>
  </div>

  <div class="contact abs" style="top:896px">
    <div class="contact-row">
      <svg viewBox="0 0 18 18"><rect width="18" height="18" rx="3" fill="#111"/><circle cx="9" cy="9" r="5" fill="none" stroke="#fff" stroke-width="1"/><ellipse cx="9" cy="9" rx="2" ry="5" fill="none" stroke="#fff" stroke-width="1"/><line x1="4" y1="9" x2="14" y2="9" stroke="#fff" stroke-width="1"/></svg>
      <div>wellbrock-office.de</div>
    </div>
  </div>
  <div class="contact abs" style="top:918px">
    <div class="contact-row">
      <svg viewBox="0 0 18 18"><rect width="18" height="18" rx="3" fill="#111"/><path d="M5 4.5l2.2-.5 1.2 2.6-1.3 1a6 6 0 0 0 3.3 3.3l1-1.3 2.6 1.2-.5 2.2C9 13 5 9 5 4.5z" fill="#fff"/></svg>
      <div>+49 (0)160 123 456 78</div>
    </div>
  </div>
  <div class="contact abs" style="top:940px">
    <div class="contact-row">
      <svg viewBox="0 0 18 18"><rect width="18" height="18" rx="3" fill="#111"/><rect x="4" y="5.5" width="10" height="7" fill="none" stroke="#fff" stroke-width="1"/><path d="M4 5.5l5 4 5-4" fill="none" stroke="#fff" stroke-width="1"/></svg>
      <div>mail@wellbrock-office.de</div>
    </div>
  </div>
  <div class="contact abs" style="top:962px">
    <div class="contact-row">
      <svg viewBox="0 0 18 18"><rect width="18" height="18" rx="3" fill="#111"/></svg>
      <div>jwb_production</div>
    </div>
  </div>

  <div class="contact abs" style="top:1004px">
    <div class="contact-row">
      <svg viewBox="0 0 18 18"><rect width="18" height="18" rx="3" fill="#111"/><path d="M4 7l5-3 5 3z" fill="#fff"/><rect x="5" y="8" width="1.5" height="4" fill="#fff"/><rect x="8.25" y="8" width="1.5" height="4" fill="#fff"/><rect x="11.5" y="8" width="1.5" height="4" fill="#fff"/><rect x="4" y="12.5" width="10" height="1.5" fill="#fff"/></svg>
      <div>Musterbank Nordwest<br>IBAN DE00.1234.5678.9012.3456.78<br>BIC MUSTDEX1XXX</div>
    </div>
  </div>

  <div class="contact abs" style="top:1074px">
    <div class="contact-row">
      <svg viewBox="0 0 18 18"><rect width="18" height="18" rx="3" fill="#111"/><rect x="4.5" y="3.5" width="8" height="11" fill="none" stroke="#fff" stroke-width="1"/><line x1="6" y1="6.5" x2="11" y2="6.5" stroke="#fff"/><line x1="6" y1="9" x2="11" y2="9" stroke="#fff"/><line x1="6" y1="11.5" x2="9" y2="11.5" stroke="#fff"/></svg>
      <div>Jonas Wellbrock<br>Finanzamt Musterstadt<br>Steuer-Nr. 000.0000.0000<br>USt-IdNr. DE000.000.000<br><br>Amtsgericht Musterstadt HRB 00000</div>
    </div>
  </div>

  <p class="payment-note abs">Endbetrag zahlbar sofort nach Erhalt innerhalb von 10 Tagen ohne Abzug auf das genannte Konto. Die Leistung ist bereits erbracht. Der Betrag wird beim Finanzamt Musterstadt ordnungsgemäß versteuert. Eine erweiterte Aufschlüsselung der Summen und Belegkopien befinden sich ggfs. in der Anlage. Auslagen und Verpflegungsmehraufwendungen können separat in Rechnung gestellt werden.</p>

</main>
</body>
</html>
```